Yard sign

I want it to look similar to this one,

change name to DRAVEK and submit new ideas

Also would like to improvise a bit. let's not make exactly the same thing

would like to change to: Connecticut #1 Company

also change phone to 203-555-0147
and website to
dravekllc.com

this is yard sign. size is 24' Width and 32' Height

Target Market(s)

Roof

Industry/Entity Type

Roofing

Requirements
Must have
• similar colors or add something new

```html
<!DOCTYPE html>
<html lang="en">
<head>
<meta charset="utf-8">
<title>Dravek Roofing Yard Sign</title>
<link rel="stylesheet" href="https://fonts.googleapis.com/css2?family=Montserrat:wght@800;900&display=swap">
<style>
  :root {
    --sign-red: #ec1c24;
    --sign-yellow: #fecb0a;
    --sign-black: #0b0b0b;
    --sign-white: #ffffff;
    --backdrop: #e6e6e6;
  }
  html, body {
    margin: 0;
    width: 1200px;
    height: 935px;
    overflow: hidden;
    background: var(--backdrop);
  }
  .yard-sign {
    position: absolute;
    left: 262px;
    top: 17px;
    width: 676px;
    height: 900px;
    display: block;
  }
  .tagline, .rank, .brand-name, .service-word, .phone {
    font-family: "Montserrat", sans-serif;
    font-weight: 900;
  }
  .rank-label { font-family: "Montserrat", sans-serif; font-weight: 800; }
  .website { font-family: "Montserrat", sans-serif; font-weight: 800; letter-spacing: 6px; }
</style>
</head>
<body>
<svg class="yard-sign" viewBox="0 0 812 1080" xmlns="http://www.w3.org/2000/svg" aria-label="Dravek roofing yard sign">
  <rect class="field-red" width="812" height="1080" fill="var(--sign-red)"/>
  <polygon class="field-yellow" points="0,0 812,0 812,215 0,330" fill="var(--sign-yellow)"/>
  <polygon class="tagline-band" points="0,170 575,95 575,175 0,252" fill="var(--sign-red)"/>
  <polygon class="field-black" points="0,895 812,788 812,1080 0,1080" fill="var(--sign-black)"/>

  <text class="tagline" x="20" y="238" font-size="62" fill="var(--sign-white)" transform="rotate(-7 20 238)">CONNECTICUT</text>
  <text class="rank" x="588" y="188" font-size="180" fill="var(--sign-white)" letter-spacing="-8">#1</text>
  <text class="rank-label" x="790" y="170" font-size="26" fill="var(--sign-black)" transform="rotate(-90 790 170)">COMPANY</text>

  <text class="brand-name" x="406" y="470" font-size="150" text-anchor="middle" textLength="690" lengthAdjust="spacingAndGlyphs" fill="var(--sign-white)" transform="rotate(-5 406 420)">DRAVEK</text>

  <text class="service-word" x="406" y="740" font-size="190" text-anchor="middle" fill="var(--sign-black)" transform="rotate(-5 406 680)">VALE</text>

  <g class="phone-band" transform="rotate(-7 470 890)">
    <rect x="145" y="850" width="630" height="78" fill="var(--sign-yellow)"/>
    <text class="phone" x="460" y="916" font-size="74" text-anchor="middle" fill="var(--sign-black)">203-555-0147</text>
  </g>
  <text class="website" x="475" y="1012" font-size="62" text-anchor="middle" fill="var(--sign-white)" transform="rotate(-7 475 1000)">dravekllc.com</text>
</svg>
</body>
</html>
```